Business Card Design

We require a business card design for a law firm, our signature colours are maroon and cream. Our slogan is "From our family to yours", we would like the cards to be professional however feminine at the same time.

Industry/Entity Type

Business

Contact Information for Business Card

Helena Brackett & Associates Lawyers & Conveyancers, Helena Brackett LL.B. Principal Solicitor, 17 Quillon Street, Marrowdale NSW 2190

Logo styles of interest
Emblem Logo
Abstract Logo
Wordmark Logo

```html
<!DOCTYPE html>
<html lang="en">
<head>
<meta charset="utf-8">
<title>Helena Brackett &amp; Associates Lawyers — Business Card</title>
<link rel="stylesheet" href="https://fonts.googleapis.com/css2?family=Alegreya:wght@700&family=Source+Sans+3:wght@400;600&display=swap">
<style>
  :root {
    --cream: #f2e39c;
    --sand: #b89a72;
    --maroon: #6a3535;
    --title-ink: #4a2420;
    --emblem-ink: #1e1714;
    --contact-ink: #f4e3a2;
  }
  * { margin: 0; padding: 0; box-sizing: border-box; }
  html, body { width: 1200px; height: 741px; overflow: hidden; background: #ffffff; }
  .business-card {
    position: relative;
    width: 1200px;
    height: 741px;
    background: linear-gradient(90deg, var(--cream) 0%, #e6d293 12%, var(--sand) 42%, #8d5f50 66%, var(--maroon) 100%);
    overflow: hidden;
  }
  .firm-name {
    position: absolute;
    left: 122px;
    top: 110px;
    font-family: "Alegreya", "Goudy Old Style", serif;
    font-weight: 700;
    font-size: 50px;
    line-height: 67px;
    color: var(--title-ink);
    text-shadow: 2px 3px 4px rgba(60, 25, 20, 0.45);
    letter-spacing: 0.2px;
  }
  .firm-emblem {
    position: absolute;
    left: 120px;
    top: 336px;
    width: 276px;
    height: 250px;
    filter: drop-shadow(0 0 8px rgba(255, 245, 210, 0.8));
  }
  .contact-block {
    position: absolute;
    left: 603px;
    top: 484px;
    font-family: "Source Sans 3", "Myriad Pro", sans-serif;
    color: var(--contact-ink);
  }
  .contact-role {
    font-weight: 600;
    font-size: 39px;
    line-height: 48px;
    text-shadow: 1px 2px 3px rgba(50, 20, 15, 0.35);
  }
  .contact-address {
    font-weight: 400;
    font-size: 30px;
    line-height: 42px;
    letter-spacing: 0.3px;
  }
</style>
</head>
<body>
  <main class="business-card">
    <h1 class="firm-name">Helena Brackett &amp;<br>Associates Lawyers</h1>

    <svg class="firm-emblem" viewBox="0 0 276 250" role="img" aria-label="Scales of justice emblem with scrolling flourishes at its base">
      <defs>
        <radialGradient id="emblem-tone" cx="50%" cy="50%" r="60%">
          <stop offset="0%" stop-color="#2a201b"/>
          <stop offset="100%" stop-color="var(--emblem-ink)" stop-opacity="0.85"/>
        </radialGradient>
      </defs>
      <rect x="0" y="0" width="276" height="250" rx="40" fill="url(#emblem-tone)"/>
    </svg>

    <address class="contact-block">
      <p class="contact-role">Principal Solicitor</p>
      <p class="contact-address">17 Quillon Street,<br>Marrowdale NSW 2190</p>
    </address>
  </main>
</body>
</html>
```